Discreet simple classy for adult entertainment

I would like a matte black business card with gold writing for my business. Keeping it simple. Having my following:

Lana frost
Events. Entertainment. Promotions
0491726580

or alternatively could have what i had on my previous card below but i think i prefer the above as again - discretion.

Maybe a nice gold line thru the card or some other very simple design . Or not open to ideas/ can be doublesided if any good ideas with that.

included pics of my old bus card. not sure weather i want a photo on it or not. if i do it wont be the same pic. i kinda wanted a card that was discreet so if it was in someones wallet they wouldn't neccessarily realise it was from a stripper.

Target Market(s)

men

Industry/Entity Type

Business

Contact Information for Business Card

Lana frost
0491726580

Requirements
Nice to have
• i don't know i am really open to anything. im giving my cards to guys so something they can have in their wallet that is discreet preferably.

```html
<!DOCTYPE html>
<html lang="en">
<head>
<meta charset="utf-8">
<title>Lana Frost — Business Card</title>
<link rel="stylesheet" href="https://fonts.googleapis.com/css2?family=Parisienne&family=Open+Sans:ital,wght@0,400;1,300&display=swap">
<style>
  :root {
    --card-black: #000000;
    --band-grey: #3a3a3a;
    --accent-olive: #6b6000;
    --tagline-olive: #8c8013;
    --text-white: #ffffff;
    --figure-shade: #1c1c1c;
  }
  html, body {
    margin: 0;
    padding: 0;
    width: 1200px;
    height: 750px;
    overflow: hidden;
    background: var(--card-black);
  }
  .card {
    position: relative;
    width: 1200px;
    height: 750px;
    background: var(--card-black);
    overflow: hidden;
  }
  .figure-area {
    position: absolute;
    left: 60px;
    top: 0;
    width: 450px;
    height: 750px;
    background: radial-gradient(ellipse 55% 60% at 45% 40%, var(--figure-shade) 0%, rgba(28,28,28,0.6) 55%, rgba(0,0,0,0) 100%);
  }
  .name-band {
    position: absolute;
    left: 480px;
    top: 67px;
    width: 668px;
    height: 274px;
    background: linear-gradient(to right, rgba(58,58,58,0) 0%, rgba(58,58,58,0.55) 45%, var(--band-grey) 100%);
  }
  .accent-bar {
    position: absolute;
    right: 0;
    top: 0;
    width: 53px;
    height: 750px;
    background: var(--accent-olive);
  }
  .name {
    position: absolute;
    margin: 0;
    font-family: "Parisienne", cursive;
    font-weight: 400;
    font-size: 120px;
    line-height: 1;
    color: var(--text-white);
  }
  .name--first { left: 520px; top: 70px; }
  .name--last { left: 790px; top: 180px; }
  .phone {
    position: absolute;
    right: 105px;
    top: 578px;
    margin: 0;
    font-family: "Open Sans", sans-serif;
    font-weight: 400;
    font-size: 56px;
    line-height: 1;
    color: var(--text-white);
  }
  .tagline {
    position: absolute;
    right: 105px;
    top: 660px;
    margin: 0;
    font-family: "Open Sans", sans-serif;
    font-style: italic;
    font-weight: 300;
    font-size: 48px;
    line-height: 1;
    color: var(--tagline-olive);
    white-space: nowrap;
  }
</style>
</head>
<body>
  <div class="card">
    <div class="figure-area" role="img" aria-label="Dark silhouette of a posing woman"></div>
    <div class="name-band"></div>
    <p class="name name--first">Lana</p>
    <p class="name name--last">Frost</p>
    <p class="phone">0491 726 580</p>
    <p class="tagline">Events, Entertainment, Promotions.</p>
    <div class="accent-bar"></div>
  </div>
</body>
</html>
```